New Stationery and envelope Design Project

I need business envelopes and stationary. I would like to have office locations on both (only Chicago address) which are Halvern (Glen Arbor), Westmoor, Mexico City, Alvoria. Of course in formats I can upload and have printed. Simple and very professional I am looking for. The return address/stationary address should be:

2867 North Pellam Avenue
Annex Level
Glen Arbor, Lakeshire 60871

Target Market(s)

I am a consultant for larger corporations

Industry/Entity Type

Consulting

Colors

Designer to choose colors to be used in the design.

Requirements
Must have
• our address, logo, very professional and clean.
Nice to have
• the names of the cities we have offices.

```html
<!DOCTYPE html>
<html lang="en">
<head>
<meta charset="utf-8">
<title>Harbor Line Global – Stationery Set</title>
<link rel="stylesheet" href="https://fonts.googleapis.com/css2?family=Ubuntu:wght@400;500&display=swap">
<style>
  :root {
    --backdrop: #f0f0f0;
    --paper: #ffffff;
    --band: #0a88d8;
    --brand: #1757c4;
    --mark: #12a0ea;
    --ink: #1f1f1f;
    --shadow: 0 0 2px rgba(0,0,0,0.12);
  }
  * { margin: 0; padding: 0; box-sizing: border-box; }
  html, body {
    width: 1200px; height: 1200px; overflow: hidden;
    background: var(--backdrop);
    font-family: "Ubuntu", sans-serif;
  }
  .canvas { position: relative; width: 1200px; height: 1200px; }
  .sheet {
    position: absolute; background: var(--paper);
    box-shadow: var(--shadow); overflow: hidden;
  }
  .brand-dot { position: absolute; border-radius: 50%; background: var(--mark); }
  .corner-disc { position: absolute; border-radius: 50%; background: var(--mark); z-index: 2; }
  .brand-name {
    position: absolute; color: var(--brand); font-weight: 400;
    white-space: nowrap; letter-spacing: 0.01em;
  }
  .address { position: absolute; color: var(--ink); line-height: 1.2; white-space: nowrap; }
  .office-band { position: absolute; left: 0; right: 0; background: var(--band); z-index: 1; }
  .office-list { position: absolute; color: #fff; white-space: nowrap; }

  /* Letterhead */
  .letterhead { left: 56px; top: 246px; width: 514px; height: 725px; }
  .letterhead .brand-dot { left: 100px; top: 64px; width: 54px; height: 54px; }
  .letterhead .brand-name { left: 127px; top: 132px; transform: translateX(-50%); font-size: 13px; }
  .letterhead .address { right: 61px; top: 107px; font-size: 10.5px; text-align: right; line-height: 12.5px; }
  .letterhead .office-band { top: 701px; height: 25px; }
  .letterhead .office-list { left: 45px; top: 6px; font-size: 10px; }
  .letterhead .corner-disc { left: 398px; top: 604px; width: 116px; height: 116px; }

  /* Business card, front */
  .card-front { left: 653px; top: 250px; width: 234px; height: 134px; border-radius: 3px; }
  .card-front .brand-dot { left: 176px; top: 17px; width: 28px; height: 28px; }
  .card-front .brand-name { right: 9px; top: 56px; font-size: 7.5px; }
  .card-front .address { right: 9px; top: 79px; font-size: 5.8px; text-align: right; line-height: 7.8px; }
  .card-front .office-band { top: 118px; height: 16px; }
  .card-front .office-list { right: 9px; top: 5px; font-size: 5px; }
  .card-front .corner-disc { left: 0; top: 73px; width: 62px; height: 62px; }

  /* Business card, back */
  .card-back { left: 911px; top: 250px; width: 234px; height: 134px; border-radius: 3px; }
  .card-back .brand-dot { left: 176px; top: 78px; width: 28px; height: 28px; }
  .card-back .brand-name { left: 188px; top: 117px; transform: translateX(-50%); font-size: 7.5px; }
  .card-back .corner-disc { left: -3px; top: -2px; width: 140px; height: 140px; }

  /* Envelope, back with flap */
  .envelope-back { left: 646px; top: 442px; width: 500px; height: 251px; }
  .envelope-back .flap { position: absolute; left: 0; top: 0; width: 500px; height: 89px; }
  .envelope-back .brand-dot { left: 238px; top: 35px; width: 24px; height: 24px; background: #fff; }
  .envelope-back .brand-name { left: 250px; top: 68px; transform: translateX(-50%); font-size: 6.5px; color: #fff; }

  /* Envelope, front */
  .envelope-front { left: 646px; top: 722px; width: 500px; height: 251px; }
  .envelope-front .brand-dot { left: 48px; top: 26px; width: 40px; height: 40px; }
  .envelope-front .brand-name { left: 26px; top: 74px; font-size: 8.5px; }
  .envelope-front .address { left: 26px; top: 92px; font-size: 7.5px; line-height: 9px; }
  .envelope-front .office-band { top: 227px; height: 24px; }
  .envelope-front .office-list { left: 26px; top: 7px; font-size: 7.5px; }
  .envelope-front .corner-disc { left: 364px; top: 112px; width: 136px; height: 136px; }
</style>
</head>
<body>
<main class="canvas">

  <section class="sheet letterhead">
    <span class="brand-dot"></span>
    <span class="brand-name">HARBOR LINE GLOBAL</span>
    <p class="address">2867 North Pellam Avenue<br>Annex Level Glen Arbor,<br>Lakeshire 60871</p>
    <span class="corner-disc"></span>
    <div class="office-band"><span class="office-list">Halvern (Glen Arbor) | Westmoor | Port Calera | Alvoria</span></div>
  </section>

  <section class="sheet card-front">
    <span class="brand-dot"></span>
    <span class="brand-name">HARBOR LINE GLOBAL</span>
    <p class="address">2867 North Pellam Avenue<br>Annex Level Glen Arbor,<br>Lakeshire 60871</p>
    <span class="corner-disc"></span>
    <div class="office-band"><span class="office-list">Halvern (Glen Arbor) | Westmoor | Port Calera | Alvoria</span></div>
  </section>

  <section class="sheet card-back">
    <span class="corner-disc"></span>
    <span class="brand-dot"></span>
    <span class="brand-name">HARBOR LINE GLOBAL</span>
  </section>

  <section class="sheet envelope-back">
    <svg class="flap" viewBox="0 0 500 89" aria-hidden="true">
      <path d="M0 0 H500 L482 64 Q474 89 448 89 H52 Q26 89 18 64 Z" fill="var(--band)"/>
    </svg>
    <span class="brand-dot"></span>
    <span class="brand-name">HARBOR LINE GLOBAL</span>
  </section>

  <section class="sheet envelope-front">
    <span class="brand-dot"></span>
    <span class="brand-name">HARBOR LINE GLOBAL</span>
    <p class="address">2867 North Pellam Avenue<br>Annex Level Glen Arbor,<br>Lakeshire 60871</p>
    <span class="corner-disc"></span>
    <div class="office-band"><span class="office-list">Halvern (Glen Arbor) | Westmoor | Port Calera | Alvoria</span></div>
  </section>

</main>
</body>
</html>
```